Bar Wanderlight VIP Card design

Looking for a design for a VIP card forguests wishing to purchase to avoid cover charges, skipping the line and othe advantages.

We used our logo on last years card.I've also attached a few of our previous cards. Looking for something fresh.

We are not apposed to a vertical card either way would be fine We will have to incorporate the fizz mild logo on the card as well.

Industry/Entity Type

Bar Restaurant www.bar-w.example

Font styles to use
Decorative

```html
<!DOCTYPE html>
<html lang="en">
<head>
<meta charset="utf-8">
<title>Bar Wanderlight VIP Card</title>
<link href="https://fonts.googleapis.com/css2?family=Playfair+Display:wght@400;700&display=swap" rel="stylesheet">
<style>
  :root {
    --backdrop: #e4e4e4;
    --card-black: #000000;
    --gold-light: #e6c21a;
    --gold-mid: #d9ae16;
    --gold-deep: #c48a10;
    --gold-ink: #b8900f;
    --gold-line: #c8961a;
  }
  * { margin: 0; padding: 0; box-sizing: border-box; }
  html, body {
    width: 1200px;
    height: 1199px;
    overflow: hidden;
    background: var(--backdrop);
  }
  .vip-card {
    position: absolute;
    left: 290px;
    top: 56px;
    width: 620px;
    height: 1087px;
    background: var(--card-black);
    overflow: hidden;
    font-family: "Playfair Display", serif;
  }
  .card-art {
    position: absolute;
    inset: 0;
    width: 620px;
    height: 1087px;
  }
  .venue-name {
    position: absolute;
    left: 60px;
    top: 108px;
    display: flex;
    align-items: center;
    gap: 12px;
    color: var(--gold-light);
    font-family: "Playfair Display", serif;
    font-weight: 700;
    font-size: 27px;
    letter-spacing: 0.5px;
  }
  .venue-dot {
    width: 18px;
    height: 18px;
    border-radius: 50%;
    background: var(--gold-light);
  }
  .vip-title {
    position: absolute;
    left: 44px;
    top: 336px;
    font-family: "Playfair Display", serif;
    font-weight: 400;
    font-size: 318px;
    line-height: 1;
    letter-spacing: 6px;
    color: var(--gold-ink);
    text-shadow: 2px 3px 3px rgba(90, 60, 0, 0.45), -1px -1px 1px rgba(255, 240, 150, 0.5);
  }
  .vip-year {
    position: absolute;
    left: 132px;
    top: 676px;
    font-family: "Playfair Display", serif;
    font-weight: 700;
    font-size: 92px;
    line-height: 1;
    color: var(--gold-ink);
    text-shadow: 2px 3px 3px rgba(90, 60, 0, 0.45), -1px -1px 1px rgba(255, 240, 150, 0.5);
  }
  .sponsor-name {
    position: absolute;
    right: 48px;
    top: 990px;
    color: var(--gold-light);
    font-family: "Playfair Display", serif;
    font-weight: 400;
    font-size: 22px;
    line-height: 1;
    white-space: nowrap;
  }
</style>
</head>
<body>
  <div class="vip-card">
    <svg class="card-art" viewBox="0 0 620 1087" xmlns="http://www.w3.org/2000/svg" aria-hidden="true">
      <defs>
        <linearGradient id="goldBand" x1="0" y1="0" x2="0.35" y2="1">
          <stop offset="0" stop-color="#e6c21a"/>
          <stop offset="0.55" stop-color="#d9ae16"/>
          <stop offset="1" stop-color="#c48a10"/>
        </linearGradient>
      </defs>
      <polygon class="gold-band" points="0,382 620,93 620,713 0,1038" fill="url(#goldBand)"/>
      <rect class="gold-frame" x="24" y="24" width="572" height="1039" fill="none" stroke="#c8961a" stroke-width="2"/>
    </svg>

    <div class="venue-name"><span class="venue-dot"></span>Bar Wanderlight</div>

    <div class="vip-title">VIP</div>
    <div class="vip-year">2023</div>

    <div class="sponsor-name">Tidewater Brewing</div>
  </div>
</body>
</html>
```